Tidewell Oyster-new seafood raw bar restaurant menu

We are a Local Seafood & Raw Bar restaurant that is looking to open in 3 months. I need-Dinner Menu Design, Happy Hour Menu, Cocktail Menu, Brunch Menu, Lunch Menu. I'd like to have you start w/ the dinner menu first then whomever I choose will also do the rest of my menus. The SHELLHOUSE by Kelpcove menu is the direction im going for as far as font organization. Id like you to give us our own personal touch. Ive also provided a mock menu that a local designer started that can't finish due to timing.

Target Market(s)

mid to high end casual seafood restaurant

Industry/Entity Type

restaurant

Font styles to use
Serif
Sans Serif

Colors
0054AA
0677BA
7BADD7
CADEEF
E8F1F8
0094D4
00A9DD
6FCCEA
C7EBF8
E9F6FB
00AB8E
00BBA5
67D7C9
C6EFE9
E9F9F6

Requirements
Must have
• 11" x 14" size

```html
<!DOCTYPE html>
<html lang="en">
<head>
<meta charset="UTF-8">
<title>Tidewell Oyster — Dinner Menu</title>
<link href="https://fonts.googleapis.com/css2?family=Bebas+Neue&family=Oswald:wght@400;500;600&family=Josefin+Sans:wght@700&family=Crimson+Pro:wght@400;600&display=swap" rel="stylesheet">
<style>
  :root{
    --navy:#163a6e;
    --navy-deep:#12305d;
    --teal-text:#48bccf;
    --panel-teal:#74cde0;
    --panel-border:#a9e0ec;
    --footer:#62c6d9;
    --white:#ffffff;
    --ink:#1d3d72;
  }
  *{margin:0;padding:0;box-sizing:border-box}
  html,body{width:1200px;height:728px;overflow:hidden;background:var(--white)}
  .menu{position:relative;width:1200px;height:728px;overflow:hidden;background:var(--white)}

  .band{position:absolute;left:0;width:1200px}
  .band--top{top:0;height:230px}
  .band--bottom{top:630px;height:98px}

  /* header */
  .brand-badge{position:absolute;left:28px;top:47px;width:100px;height:100px;border-radius:50%;
    border:3px solid var(--white);display:flex;align-items:center;justify-content:center;text-align:center;
    font-family:'Oswald',sans-serif;font-weight:500;font-size:13px;line-height:1.15;color:var(--white);letter-spacing:1px}
  .headline{position:absolute;left:174px;top:36px;font-family:'Bebas Neue',sans-serif;color:var(--white);
    font-size:50px;line-height:44px;letter-spacing:1px}
  .headline .plate{display:inline-block;width:62px;height:36px;border-radius:50%;background:#c9d6e6;vertical-align:-3px;margin:0 1px}

  .raw-col{position:absolute;top:42px;color:var(--white)}
  .raw-item{margin-bottom:7px}
  .raw-item h3{font-family:'Oswald',sans-serif;font-weight:500;font-size:15px;line-height:16px;letter-spacing:.6px;text-transform:uppercase}
  .raw-item p,.raw-item li{font-family:'Crimson Pro',serif;font-size:13.5px;line-height:16px;padding-left:16px;list-style:none}
  .price-row{display:flex;justify-content:space-between;width:128px}
  .price-row.sm{width:128px}
  .build-own{position:absolute;left:963px;top:148px;width:198px;height:30px;border:2px solid #8fa6c6;
    font-family:'Oswald',sans-serif;font-weight:500;font-size:15px;letter-spacing:1.5px;color:var(--white);
    display:flex;align-items:center;justify-content:center}
  .build-own .coin{position:absolute;right:-12px;bottom:-12px;width:18px;height:18px;border-radius:50%;
    background:var(--white);color:var(--navy);font-family:'Crimson Pro',serif;font-size:11px;display:flex;align-items:center;justify-content:center;letter-spacing:0}

  /* panels */
  .panel{position:absolute;top:255px;height:343px;border-radius:14px}
  .panel--smaller{left:43px;width:542px;background:var(--white);border:5px solid var(--panel-border)}
  .panel--signature{left:614px;width:543px;background:var(--panel-teal)}
  .panel-title{position:absolute;font-family:'Josefin Sans',sans-serif;font-weight:700}
  .panel--smaller .panel-title{left:0;right:0;top:18px;text-align:center;font-size:28px;letter-spacing:7px;color:var(--teal-text)}
  .panel--signature .panel-title{left:288px;top:283px;font-family:'Bebas Neue',sans-serif;font-weight:400;font-size:44px;letter-spacing:2px;color:var(--white)}

  .dish-col{position:absolute}
  .dish{margin-bottom:5px}
  .dish h4{font-family:'Oswald',sans-serif;font-weight:500;font-size:15.5px;line-height:17px;letter-spacing:.6px;text-transform:uppercase}
  .dish p{font-family:'Oswald',sans-serif;font-weight:400;font-size:10.5px;line-height:13px;letter-spacing:.5px;text-transform:uppercase}
  .panel--smaller .dish{color:var(--teal-text)}
  .panel--smaller .dish-col{top:64px}
  .panel--smaller .dish-col--a{left:18px;width:240px}
  .panel--smaller .dish-col--b{left:264px;width:270px}
  .panel--signature .dish{color:var(--ink)}
  .panel--signature .dish-col{top:36px}
  .panel--signature .dish-col--a{left:29px;width:250px}
  .panel--signature .dish-col--b{left:288px;width:250px}

  /* footer */
  .kids{position:absolute;left:34px;top:668px;display:flex;align-items:baseline;gap:22px;color:var(--navy);font-family:'Bebas Neue',sans-serif}
  .kids h2{font-size:44px;font-weight:400;letter-spacing:1px;margin-right:8px}
  .kids span{font-size:28px;letter-spacing:.5px}
  .footer-brand{position:absolute;left:958px;top:670px;display:flex;align-items:center;gap:10px;color:var(--white);
    font-family:'Oswald',sans-serif;font-weight:600;font-size:20px;line-height:20px;letter-spacing:1px}
  .footer-brand .dot{width:24px;height:24px;border-radius:50%;background:var(--white)}
</style>
</head>
<body>
<main class="menu">
  <svg class="band band--top" viewBox="0 0 1200 230" preserveAspectRatio="none" aria-hidden="true">
    <path fill="var(--navy)" d="M0 0H1200V218L1150 214 1080 220 1010 213 940 219 860 215 780 221 700 214 620 220 540 213 460 218 380 214 300 221 220 215 140 220 60 213 0 218Z"/>
  </svg>
  <svg class="band band--bottom" viewBox="0 0 1200 98" preserveAspectRatio="none" aria-hidden="true">
    <path fill="var(--footer)" d="M0 8L70 4 150 10 230 5 320 11 400 4 490 9 570 5 660 11 740 4 830 9 910 5 1000 10 1080 4 1150 9 1200 6V98H0Z"/>
  </svg>

  <div class="brand-badge">TIDEWELL<br>OYSTER</div>
  <h1 class="headline">RAW BAR/<br>CHILLED<br>SEAF<span class="plate" role="img" aria-label="Illustration of an oyster platter on ice"></span>D</h1>

  <section class="raw-col" style="left:378px">
    <div class="raw-item">
      <h3>Oyster Chef's<br>Preparation</h3>
      <ul>
        <li style="padding-left:0">Oyster selection</li>
        <li class="price-row"><span>House</span><span>$</span></li>
        <li class="price-row"><span>East Coast</span><span>$</span></li>
        <li class="price-row"><span>Regional</span><span>$</span></li>
        <li>Accompaniments,<br>top'em</li>
      </ul>
    </div>
  </section>
  <section class="raw-col" style="left:554px">
    <div class="raw-item" style="margin-bottom:10px">
      <h3>Seafood Tower</h3>
      <ul>
        <li class="price-row"><span>Small</span><span>$</span></li>
        <li class="price-row"><span>Large</span><span>$</span></li>
      </ul>
    </div>
    <div class="raw-item">
      <h3>Ceviche</h3>
      <p>Citrus, fruit, peppers,<br>onion, cilantro</p>
    </div>
  </section>
  <section class="raw-col" style="left:750px">
    <div class="raw-item">
      <h3>Tuna Poke/Crudo</h3>
      <p>Ponzu, scallions, ginger,<br>avocado, sesame</p>
    </div>
    <div class="raw-item">
      <h3>Scallop Crudo</h3>
      <p>Lemon, ginger, chives,<br>olive oil, pine nuts</p>
    </div>
  </section>
  <section class="raw-col" style="left:963px">
    <div class="raw-item" style="margin-bottom:4px">
      <h3>Peel and Eat Shrimp</h3>
      <p>Remoulade, tartar, cocktail</p>
    </div>
    <div class="raw-item" style="margin-bottom:4px">
      <h3>Local Fish Crudo</h3>
      <p>Seasonal accompaniments</p>
    </div>
    <div class="raw-item"><h3>Cured Salmon</h3></div>
  </section>
  <div class="build-own">BUILD YOUR OWN<span class="coin">$</span></div>

  <section class="panel panel--smaller">
    <h2 class="panel-title">SMALLER</h2>
    <div class="dish-col dish-col--a">
      <div class="dish"><h4>Fried Shrimp</h4><p>Remoulade</p></div>
      <div class="dish"><h4>Mussels</h4><p>Local bacon, shallot, garlic,<br>tomato, spicy herb butter</p></div>
      <div class="dish"><h4>Roasted Oysters</h4><p>½ dozen, choice of Rockefeller,<br>Bienville, Tidewell special</p></div>
      <div class="dish"><h4>Shrimp and Grits</h4><p>Local andouille, roasted peppers,<br>garlic, shallot, charred tomato</p></div>
      <div class="dish"><h4>Crab Mac'n Cheese</h4><p>Cheddar, fontina, cotija,<br>local pasta shells</p></div>
      <div class="dish"><h4>Shrimp Remoulade</h4><p>Avocado, fried green tomato</p></div>
    </div>
    <div class="dish-col dish-col--b">
      <div class="dish" style="margin-bottom:3px"><h4>Pumpkin Risotto</h4><p>Herbs, dried cherry, local mushrooms</p></div>
      <div class="dish" style="margin-bottom:3px"><h4>Caeser</h4><p>Baby gem lettuce, parmesan</p></div>
      <div class="dish"><h4>Greenrow Crisp<br>Greens Salad</h4><p>Fig, goat cheese, spiced pepitos,<br>sour cherry vinaigrette</p></div>
      <div class="dish"><h4>Clam Chowder</h4><p>New England style</p></div>
      <div class="dish"><h4>Baja Fish Tacos</h4><p>Slaw, cilantro, lime</p></div>
      <div class="dish"><h4>Steak Taco</h4><p>Mojo, dried chili salsa, pickled onion,<br>cotija</p></div>
    </div>
  </section>

  <section class="panel panel--signature">
    <div class="dish-col dish-col--a">
      <div class="dish"><h4>Clam Linguini</h4><p>Local pasta. local bacon, peppers,<br>butter, herbs</p></div>
      <div class="dish"><h4>Vegetable Gnocchi</h4><p>Squash, shallots, peas, mushroom,<br>basil, parmesan</p></div>
      <div class="dish"><h4>Pan Seared Scallops</h4><p>Curry, cauliflower, carrots,<br>eggplant, Carolina gold rice</p></div>
      <div class="dish"><h4>Halibut Gumbo</h4><p>Shrimp, scallions, okra garnish</p></div>
      <div class="dish"><h4>Grilled Steak</h4><p>Roasted rainbow carrots, mashed<br>potatoes, ancho demi, chimichurri</p></div>
      <div class="dish"><h4>Surf and Turf Filet</h4><p>Asparagus, baby potatoes,<br>bearnaise, demi</p></div>
      <div class="dish"><h4>Fresh Catch Crab Legs</h4><p>Butter, cocktail, spicy remoulade</p></div>
    </div>
    <div class="dish-col dish-col--b">
      <div class="dish"><h4>Lowcountry Boil</h4><p>Shrimp, sausage, corn, potato</p></div>
      <div class="dish"><h4>Smash Burger</h4><p>Spicy “thousand island”, pickles,<br>house cut fries, LTO</p></div>
      <div class="dish"><h4>Lobster Roll</h4><p>Lots of lobstah, scallions, celery,<br>house fries</p></div>
      <div class="dish"><h4>Fish Sandwich</h4><p>Lots of lobstah, scallions, celery,<br>house fries</p></div>
      <div class="dish"><h4>Fish Sandwich</h4><p>Double stacked halibut,<br>pickled carrots, lemon/caper/dill<br>aioli, lettuce, tomato</p></div>
    </div>
    <h2 class="panel-title">SIGNATURE</h2>
  </section>

  <footer>
    <div class="kids">
      <h2>KIDS</h2>
      <span>Chicken Tenders</span><span>Mac N Cheese</span><span>Fried Fish</span><span>Fried Shrimp</span>
    </div>
    <div class="footer-brand"><span class="dot"></span><span>TIDEWELL OYSTER<br>SEAFOOD RAW BAR</span></div>
  </footer>
</main>
</body>
</html>
```